Packaging design (small box) for Zelkor 5/6 cable (keychain cable)

we need a packaging to sell our cellphone cable.

1)I want the word "BRIX" on the life side in a stylish way...
2)The product must be mostly visible (not hidden with graphic or design)
3)Please design the sides of the packaging (colors,graphics,etc)
4)Please integrate my logo on the packaging (files 3) you can change the colour of the logo if you want.
Please check the attached files: The packaging will be exactly like this with the same material and size (file 2) (the design on the packaging of this picture is the degin by defaut from our supplier).

-They will be put in a counterdisplay

Size of the packaging:
W:36mm H:130mm D:17mm
We trust your creativity!

Attached files the sketch of our packaging and our products to inspire you.

Target Market(s)

16-35 male and female

Industry/Entity Type

Product

Requirements
Must have
• We need the following words on the packaging:
• 1)"Câble compatible pour Zelkor 5/6 " (on the front)
• 2) Recharge rapidement (meaning:charge fast)
• 3) Toujours à portée de la main ( meaning always with you)
• 4)BRIX on the left side
• 5)Our logo "Vantoro"
Nice to have
• I am really open about your ideas
Should not have

```html
<!DOCTYPE html>
<html lang="fr">
<head>
<meta charset="utf-8">
<title>BRIX – Vantoro keychain cable box dieline</title>
<link rel="stylesheet" href="https://fonts.googleapis.com/css2?family=Montserrat:wght@800&family=Open+Sans:wght@400;600&display=swap">
<style>
  :root{
    --navy:#1b2a4e;
    --navy-deep:#172443;
    --blue-mid:#2a5592;
    --blue-glow:#3a7cc0;
    --cut:#41b8d8;
    --ink:#222428;
    --white:#ffffff;
  }
  html,body{margin:0;padding:0;overflow:hidden;background:var(--white);}
  .canvas{width:1038px;height:1200px;position:relative;overflow:hidden;}
  .dieline{display:block;}
  .cut-line{fill:none;stroke:var(--cut);stroke-width:1;}
  .fold-line{stroke:var(--cut);stroke-width:.8;opacity:.8;}
  .side-word{font-family:"Montserrat",sans-serif;font-weight:800;font-size:60px;fill:var(--white);letter-spacing:4px;}
  .brand-name{font-family:"Open Sans",sans-serif;font-weight:400;letter-spacing:2px;}
  .brand-name--front{font-size:29px;fill:var(--ink);}
  .brand-name--back{font-size:19px;fill:var(--white);}
  .copy{font-family:"Open Sans",sans-serif;font-weight:400;fill:var(--white);}
  .copy--front{font-size:20px;}
  .copy--back{font-size:16.5px;}
  .icon-stroke{fill:none;stroke:var(--white);stroke-width:4.5;}
  .icon-fill{fill:var(--white);}
</style>
</head>
<body>
<div class="canvas">
<svg class="dieline" width="1038" height="1200" viewBox="0 0 1038 1200" xmlns="http://www.w3.org/2000/svg">
  <defs>
    <linearGradient id="panel-vertical" x1="0" y1="0" x2="0" y2="1">
      <stop offset="0" stop-color="var(--navy)"/>
      <stop offset=".18" stop-color="var(--navy)"/>
      <stop offset=".5" stop-color="var(--blue-mid)"/>
      <stop offset=".82" stop-color="var(--navy)"/>
      <stop offset="1" stop-color="var(--navy-deep)"/>
    </linearGradient>
    <radialGradient id="side-glow" cx="820" cy="600" r="330" gradientUnits="userSpaceOnUse">
      <stop offset="0" stop-color="var(--blue-glow)" stop-opacity=".85"/>
      <stop offset="1" stop-color="var(--blue-glow)" stop-opacity="0"/>
    </radialGradient>
    <radialGradient id="band-glow" cx="394" cy="940" r="110" gradientUnits="userSpaceOnUse">
      <stop offset="0" stop-color="var(--blue-glow)" stop-opacity=".9"/>
      <stop offset="1" stop-color="var(--blue-glow)" stop-opacity="0"/>
    </radialGradient>
    <radialGradient id="tab-glow" cx="690" cy="215" r="100" gradientUnits="userSpaceOnUse">
      <stop offset="0" stop-color="var(--blue-glow)"/>
      <stop offset="1" stop-color="var(--navy)"/>
    </radialGradient>
    <radialGradient id="dots-tone" cx=".5" cy=".45" r=".5">
      <stop offset="0" stop-color="#6f8fbf" stop-opacity=".45"/>
      <stop offset="1" stop-color="#6f8fbf" stop-opacity="0"/>
    </radialGradient>
  </defs>

  <!-- printed body -->
  <g class="print-body">
    <rect x="198" y="244" width="652" height="724" fill="url(#panel-vertical)"/>
    <rect x="494" y="244" width="356" height="724" fill="url(#side-glow)"/>
    <rect class="window-panel" x="294" y="244" width="200" height="606" fill="var(--white)"/>
    <rect class="front-band-glow" x="294" y="850" width="200" height="118" fill="url(#band-glow)"/>
    <path class="hang-tab" d="M589 244 V162 Q589 149 602 149 H777 Q790 149 790 162 V244 Z" fill="url(#tab-glow)"/>
    <path class="hang-hole" d="M651 193 H676 A14 14 0 0 1 704 193 H726 A10.5 10.5 0 0 1 726 214 H651 A10.5 10.5 0 0 1 651 193 Z" fill="var(--white)"/>
    <rect class="dot-field" x="512" y="712" width="328" height="228" fill="url(#dots-tone)" role="img" aria-label="Halftone dot pattern fading out around the back panel"/>
  </g>

  <!-- left side: brand word -->
  <text class="side-word" transform="translate(226 604) rotate(90)" text-anchor="middle">BRIX</text>

  <!-- front panel -->
  <g class="front-brand">
    <circle cx="408" cy="712" r="58" fill="var(--blue-mid)"/>
    <text class="brand-name brand-name--front" x="386" y="806" text-anchor="middle">VANTORO</text>
  </g>
  <text class="copy copy--front" x="392" y="894" text-anchor="middle">Câble compatible</text>
  <text class="copy copy--front" x="392" y="920" text-anchor="middle">pour Zelkor 5/6</text>

  <!-- back panel -->
  <g class="back-brand">
    <circle cx="698" cy="372" r="40" fill="var(--white)"/>
    <text class="brand-name brand-name--back" x="683" y="439" text-anchor="middle">VANTORO</text>
  </g>
  <text class="copy copy--back" x="688" y="486" text-anchor="middle">Câble compatible</text>
  <text class="copy copy--back" x="688" y="507" text-anchor="middle">pour Zelkor 5/6</text>

  <g class="icon-charge">
    <circle class="icon-stroke" cx="688" cy="584" r="31"/>
    <path class="icon-fill" d="M693 563 L676 588 H687 L682 606 L700 579 H689 Z"/>
  </g>
  <text class="copy copy--back" x="688" y="654" text-anchor="middle">Recharge</text>
  <text class="copy copy--back" x="688" y="675" text-anchor="middle">rapidement</text>

  <g class="icon-keyring">
    <circle class="icon-stroke" cx="669" cy="718" r="13" stroke-width="3.5"/>
    <rect class="icon-fill" x="674" y="717" width="54" height="15" rx="7.5" transform="rotate(12 700 724)"/>
  </g>
  <text class="copy copy--back" x="688" y="771" text-anchor="middle">Toujours à portée</text>
  <text class="copy copy--back" x="688" y="792" text-anchor="middle">de la main</text>

  <!-- cut and fold lines -->
  <g class="cuts">
    <path class="cut-line" d="M294 244 V136 Q294 116 314 116 H474 Q494 116 494 136 V244"/>
    <path class="cut-line" d="M294 160 H494 M334 160 l3 9 M454 160 l-3 9"/>
    <path class="cut-line" d="M198 244 V222 L210 215 V178 Q210 170 218 170 H278 Q284 170 284 178 V238 L294 244"/>
    <path class="cut-line" d="M494 244 L504 237 V178 Q504 170 512 170 H570 Q576 170 576 178 V215 L589 222"/>
    <path class="cut-line" d="M294 968 V1076 Q294 1096 314 1096 H474 Q494 1096 494 1076 V968"/>
    <path class="cut-line" d="M294 1050 H494 M334 1050 l3 -9 M454 1050 l-3 -9"/>
    <path class="cut-line" d="M198 968 V990 L210 997 V1032 Q210 1040 218 1040 H278 Q284 1040 284 1032 V974 L294 968"/>
    <path class="cut-line" d="M494 968 L504 975 V1032 Q504 1040 512 1040 H570 Q576 1040 576 1032 V997 L589 990 V968"/>
    <path class="cut-line" d="M790 244 L850 250 V962 L790 968"/>
    <rect class="cut-line" x="198" y="244" width="592" height="724"/>
    <line class="fold-line" x1="294" y1="244" x2="294" y2="968"/>
    <line class="fold-line" x1="494" y1="244" x2="494" y2="968"/>
    <line class="fold-line" x1="589" y1="244" x2="589" y2="968"/>
  </g>
</svg>
</div>
</body>
</html>
```